Modern Label Design needed for Virgin Coconut Oil bottle

Label for organic virgin coconut oil. Must be unique, creative, modern and give the impression of an expensive premium product.
Label is for round containers (bottles and jars) 250 ml, 500 ml and 750 ml.
The Brand name is "Mont Verane" and the product stated must include the words "organic" "cold-pressed" and "virgin coconut oil".
Label must include the following product description:
"Mont Verane virgin coconut oil is made from fresh mature coconuts harvested from organic farms across the Caribbean region. The oil is produced using the traditional natural fermentation method. Absolutely no heat is used in the process to allow for the maximum possible content of lauric acid."
Additional info: "Product of Tobago" "Manufactured and bottled by Sunmere Harvest Ltd., Barrow Agro-Commercial Estate, Lowlands Tobago".
Label must include room for Best Before date, Batch number, barcode and nutrition facts.
Colors can be at designer's discretion. However white, green and gold are preferred.

Target Market(s)

Women, Cosmetic Industry, (Food Industry to a lesser extent)

Industry/Entity Type

Product

Font styles to use
Script

Requirements
Must have
• An expensive look.
• The label is intended to have a transparent background
Nice to have
• The colors green and gold. However other color suggestions are welcome.
• Also, tasteful images that communicate an exotic tropical environment. (flowers, palms, coconuts

```html
<!DOCTYPE html>
<html lang="en">
<head>
<meta charset="utf-8">
<title>Mont Verane – Virgin Coconut Oil Label Variants</title>
<link rel="stylesheet" href="https://fonts.googleapis.com/css2?family=Parisienne&family=Questrial&display=swap">
<style>
  :root {
    --paper: #ffffff;
    --gold: #c9a54c;
    --green: #1f8a22;
    --green-soft: #4a9a55;
    --ink: #1a1a1a;
    --rule-dark: #3a3a3a;
    --leaf: #5f8a3c;
    --leaf-deep: #3f6b2c;
    --bloom: #e7a3a8;
    --plume-blue: #3b7fc0;
    --plume-yellow: #e0b233;
  }
  * { margin: 0; padding: 0; box-sizing: border-box; }
  html, body {
    width: 1200px;
    height: 846px;
    overflow: hidden;
    background: var(--paper);
  }
  .canvas {
    position: relative;
    width: 1200px;
    height: 846px;
    background: var(--paper);
  }
  .label {
    position: absolute;
    top: 352px;
    width: 210px;
    margin-left: -105px;
    text-align: center;
    --accent: var(--gold);
    --accent-2: var(--gold);
    --rule: var(--gold);
  }
  .label--gold { left: 200px; }
  .label--green { left: 610px; --accent: var(--green); --accent-2: var(--ink); --rule: var(--rule-dark); }
  .label--mixed { left: 1008px; --accent: var(--gold); --accent-2: var(--green-soft); --rule: var(--green-soft); }

  .brand-name {
    font-family: "Parisienne", cursive;
    font-size: 36px;
    line-height: 48px;
    font-weight: 400;
    white-space: nowrap;
    color: var(--accent);
  }
  .label--mixed .brand-name { font-size: 33px; }
  .brand-rule {
    width: 112px;
    height: 1px;
    margin: 6px auto 0;
    background: var(--rule);
  }
  .claims {
    margin-top: 12px;
    font-family: "Questrial", sans-serif;
    font-size: 9.5px;
    line-height: 13px;
    letter-spacing: 0.2px;
    color: var(--gold);
  }
  .label--green .claims { color: var(--green); }
  .label--mixed .claims { color: var(--green-soft); font-size: 10.5px; }
  .product-name {
    font-family: "Questrial", sans-serif;
    font-size: 9.5px;
    line-height: 13px;
    letter-spacing: 0.3px;
    text-transform: uppercase;
    color: var(--gold);
  }
  .label--green .product-name { color: var(--ink); }

  .tropical-scene {
    position: relative;
    width: 150px;
    height: 106px;
    margin: 8px auto 0;
  }
  .tropical-art {
    position: absolute;
    inset: 0;
    border-radius: 14px;
    background:
      radial-gradient(circle at 22% 55%, var(--leaf) 0%, rgba(95,138,60,0.55) 28%, transparent 48%),
      radial-gradient(circle at 70% 45%, var(--bloom) 0%, rgba(231,163,168,0.5) 14%, transparent 28%),
      radial-gradient(ellipse at 80% 40%, var(--plume-blue) 0%, transparent 22%),
      radial-gradient(ellipse at 82% 78%, var(--plume-yellow) 0%, transparent 26%),
      radial-gradient(circle at 62% 62%, var(--leaf-deep) 0%, transparent 30%);
    opacity: 0.85;
  }
  .volume {
    position: absolute;
    top: 26px;
    left: 50%;
    transform: translateX(-50%);
    font-family: "Questrial", sans-serif;
    font-size: 10px;
    line-height: 12px;
    white-space: nowrap;
    background: var(--paper);
    padding: 0 3px;
    color: var(--gold);
  }
  .label--green .volume { color: var(--ink); }

  .product-info {
    margin-top: 10px;
    font-family: "Questrial", sans-serif;
    font-size: 7px;
    line-height: 9.2px;
    color: var(--accent-2);
  }
  .label--gold .product-info { color: var(--gold); }
  .description { text-align: center; }
  .origin {
    margin-top: 5px;
    text-transform: uppercase;
    letter-spacing: 0.4px;
    color: var(--accent);
  }
  .maker { margin-top: 2px; }
  .info-boxes {
    display: flex;
    gap: 6px;
    margin-top: 6px;
    text-align: left;
  }
  .info-box {
    flex: 1;
    height: 46px;
    border: 0.75px solid var(--rule);
    padding: 3px 4px;
    font-size: 6.5px;
    line-height: 8.5px;
  }
  .info-box__title {
    text-transform: uppercase;
    letter-spacing: 0.3px;
    border-bottom: 0.75px solid var(--rule);
    padding-bottom: 2px;
    margin-bottom: 2px;
  }
  .info-box--code { flex: 0 0 62px; }
</style>
</head>
<body>
<main class="canvas">
  <section class="label label--gold">
    <h1 class="brand-name">Mont Verane</h1>
    <div class="brand-rule"></div>
    <p class="claims">organic • cold pressed</p>
    <p class="product-name">Virgin Coconut Oil</p>
    <div class="tropical-scene">
      <div class="tropical-art" role="img" aria-label="Watercolour palm leaves, halved coconut, hibiscus flowers and a blue and yellow macaw"></div>
      <span class="volume">250 ml</span>
    </div>
    <div class="product-info">
      <p class="description">Mont Verane virgin coconut oil is made from fresh mature coconuts harvested from organic farms across the Caribbean region. The oil is produced using the traditional natural fermentation method. Absolutely no heat is used in the process to allow for the maximum possible content of lauric acid.</p>
      <p class="origin">Product of Tobago</p>
      <p class="maker">Manufactured and bottled by Sunmere Harvest Ltd., Barrow Agro-Commercial Estate, Lowlands Tobago</p>
      <div class="info-boxes">
        <div class="info-box"><p class="info-box__title">Nutrition Facts</p></div>
        <div class="info-box info-box--code"><p>Best Before:</p><p>Batch No:</p></div>
      </div>
    </div>
  </section>

  <section class="label label--green">
    <h1 class="brand-name">Mont Verane</h1>
    <div class="brand-rule"></div>
    <p class="claims">organic • cold pressed</p>
    <p class="product-name">Virgin Coconut Oil</p>
    <div class="tropical-scene">
      <div class="tropical-art" role="img" aria-label="Watercolour palm leaves, halved coconut, hibiscus flowers and a blue and yellow macaw"></div>
      <span class="volume">250 ml</span>
    </div>
    <div class="product-info">
      <p class="description">Mont Verane virgin coconut oil is made from fresh mature coconuts harvested from organic farms across the Caribbean region. The oil is produced using the traditional natural fermentation method. Absolutely no heat is used in the process to allow for the maximum possible content of lauric acid.</p>
      <p class="origin">Product of Tobago</p>
      <p class="maker">Manufactured and bottled by Sunmere Harvest Ltd., Barrow Agro-Commercial Estate, Lowlands Tobago</p>
      <div class="info-boxes">
        <div class="info-box"><p class="info-box__title">Nutrition Facts</p></div>
        <div class="info-box info-box--code"><p>Best Before:</p><p>Batch No:</p></div>
      </div>
    </div>
  </section>

  <section class="label label--mixed">
    <h1 class="brand-name">Mont Verane</h1>
    <div class="brand-rule"></div>
    <p class="claims">organic • cold pressed</p>
    <p class="product-name">Virgin Coconut Oil</p>
    <div class="tropical-scene">
      <div class="tropical-art" role="img" aria-label="Watercolour palm leaves, halved coconut, hibiscus flowers and a blue and yellow macaw"></div>
      <span class="volume">250 ml</span>
    </div>
    <div class="product-info">
      <p class="description">Mont Verane virgin coconut oil is made from fresh mature coconuts harvested from organic farms across the Caribbean region. The oil is produced using the traditional natural fermentation method. Absolutely no heat is used in the process to allow for the maximum possible content of lauric acid.</p>
      <p class="origin">Product of Tobago</p>
      <p class="maker">Manufactured and bottled by Sunmere Harvest Ltd., Barrow Agro-Commercial Estate, Lowlands Tobago</p>
      <div class="info-boxes">
        <div class="info-box"><p class="info-box__title">Nutrition Facts</p></div>
        <div class="info-box info-box--code"><p>Best Before:</p><p>Batch No:</p></div>
      </div>
    </div>
  </section>
</main>
</body>
</html>
```